Business Card Design

Electric home brewing equipment. Custom and catalog items. Most products are made by or for my company, so name is on most everything. Travel to conventions, to meet with home brewers. Trying to create a professional, but since primarily home brewers, fun image. New logo attached, with this new logo I'm redoing most materials. I'm trying to create a single brand under this logo.
Bolt icon on card, does not have to be directly over text as in logo file, but can be used similar to my example.

Website address is http://www.kettlornworks.com (this is a must add).

New video intro to be added to video productions here: http://vidplomo.net/qz7Lm2xTrwa

Target Market(s)

Home brewers, predominantly male, ages 21 - 55, tend to be looking for the hot new thing.

Industry/Entity Type

Business

Contact Information for Business Card

Details as included on file. Layout I've attached is approximately what I'm looking for. Single and Double sided cards options welcome.

Card info should include:
2 cards: Derek Holm and Nadia Holm
Both: Owners
Email: derek@kettlornworks.com and nadia@kettlornworks.com
Both phone: 888-427-9035
Both address: Spring, Texas 77512
Website: kettlornworks.com

Requirements
Must have
• Use both parts of the logo, not necessarily together as design should infer.

```html
<!DOCTYPE html>
<html lang="en">
<head>
<meta charset="utf-8">
<title>Kettlorn Works Supply — Business Card</title>
<link rel="stylesheet" href="https://fonts.googleapis.com/css2?family=Arimo:wght@400;700&display=swap">
<style>
  :root {
    --stage: #d9d9d9;
    --card: #ffffff;
    --ink: #1a1a1a;
    --bolt-yellow: #f2d23a;
    --text-gray: #222222;
  }
  * { margin: 0; padding: 0; box-sizing: border-box; }
  html, body { width: 1200px; height: 475px; overflow: hidden; }
  body {
    background: var(--stage);
    font-family: "Arimo", Arial, sans-serif;
    color: var(--ink);
    position: relative;
  }
  .card {
    position: absolute;
    top: 89px;
    width: 520px;
    height: 297px;
    background: var(--card);
    overflow: hidden;
    box-shadow: 0 2px 6px rgba(0,0,0,0.15);
  }
  /* Back face */
  .card-back { left: 50px; }
  .card-back .dark-band {
    position: absolute; left: 0; top: 0; width: 100%; height: 148px;
    background: var(--ink);
  }
  .card-back .emblem-circle {
    position: absolute; left: 70px; top: 38px;
    width: 220px; height: 220px; border-radius: 50%;
    background: var(--card);
    border: 22px solid var(--ink);
  }
  .card-back .brand {
    position: absolute; left: 310px; top: 152px;
  }
  /* Front face */
  .card-front { left: 630px; }
  .card-front .dark-panel {
    position: absolute; left: 0; top: 0; width: 120px; height: 100%;
    background: var(--ink);
  }
  .card-front .emblem-circle {
    position: absolute; left: 22px; top: 40px;
    width: 218px; height: 218px; border-radius: 50%;
    background: var(--card);
    border: 20px solid var(--ink);
  }
  .card-front .brand {
    position: absolute; right: 26px; top: 26px; text-align: left;
  }
  .brand-name {
    font-weight: 700; font-size: 24px; letter-spacing: -0.3px;
    color: var(--ink); white-space: nowrap; line-height: 1;
  }
  .card-back .brand-name { font-size: 18px; }
  .brand-sub {
    font-weight: 700; font-size: 11px; letter-spacing: 6px;
    text-align: center; margin-top: 3px; color: var(--ink);
  }
  .card-back .brand-sub { font-size: 8px; letter-spacing: 5px; }
  .brand-location {
    font-size: 14px; margin-top: 8px; color: var(--text-gray); white-space: nowrap;
  }
  .person {
    position: absolute; right: 26px; top: 136px; text-align: right;
  }
  .person-name { font-size: 27px; color: var(--text-gray); line-height: 1.05; white-space: nowrap; }
  .person-role { font-size: 15px; color: var(--bolt-yellow); font-weight: 700; }
  .contacts {
    position: absolute; right: 22px; top: 196px; list-style: none;
  }
  .contacts li {
    display: flex; justify-content: flex-end; align-items: center;
    gap: 6px; font-size: 13px; color: var(--text-gray);
    height: 21px; margin-bottom: 2px; white-space: nowrap;
  }
  .contacts svg { width: 17px; height: 17px; flex: none; }
  .contacts svg * { fill: none; stroke: var(--bolt-yellow); stroke-width: 1.6; }
</style>
</head>
<body>

  <section class="card card-back" aria-label="Card back">
    <div class="dark-band"></div>
    <div class="emblem-circle"></div>
    <div class="brand">
      <p class="brand-name">Kettlorn Works</p>
      <p class="brand-sub">SUPPLY</p>
    </div>
  </section>

  <section class="card card-front" aria-label="Card front">
    <div class="dark-panel"></div>
    <div class="emblem-circle"></div>
    <div class="brand">
      <p class="brand-name">Kettlorn Works</p>
      <p class="brand-sub">SUPPLY</p>
      <p class="brand-location">Alder Creek, TX 77512</p>
    </div>
    <div class="person">
      <p class="person-name">Derek Holm</p>
      <p class="person-role">Owner</p>
    </div>
    <ul class="contacts">
      <li>888-427-9035
        <svg viewBox="0 0 18 18" aria-hidden="true"><rect x="5" y="1.5" width="8" height="15" rx="1.5"/><line x1="8" y1="14" x2="10" y2="14"/></svg>
      </li>
      <li>derek@kettlornworks.com
        <svg viewBox="0 0 18 18" aria-hidden="true"><rect x="1.5" y="4" width="15" height="10"/><polyline points="1.5,4 9,10 16.5,4"/></svg>
      </li>
      <li>kettlornworks.com
        <svg viewBox="0 0 18 18" aria-hidden="true"><circle cx="9" cy="9" r="7.5"/><ellipse cx="9" cy="9" rx="3.2" ry="7.5"/><line x1="1.5" y1="9" x2="16.5" y2="9"/></svg>
      </li>
    </ul>
  </section>

</body>
</html>
```